VocaTerrania Community/ Talent Gallery

VocaTerrania is developing a collaborative career course, with coaching and community exchange. Goal is to offer a platform where talented candidates can show their expertise and find projects, partners, and develop their online portfolios!

Here is a good example of the type of thing we hope to create with focus on sustainability focused talent to task matching
http://www.harrowbyquill.example/global-themes/employment-and-growth/connecting-talent-with-opportunity-in-the-digital-age

We hope to have a "grid style" gallery where it is easy to search by talent types and focus areas within the scope of "Sustainability" issues...Food/Water/Energy, Public Health, Technology, Sustainable Cities, Infrastructure, Education, Policy, Emerging Economies, Ecosystems, Social Innovation, inclusive Security, Equity Issues. For each topic/ header we hope to have candidates post their completed portfolios to exhibit resumes, biography, a case study... they may actually prepare these on other sites, but can link in OR alternately that they can easily create here, similar to "posy.lan" ....

Hope to include a blog space titled "Walking the Ridge", where people can mix it up across these topic issues as they are interdependent and often require partners across discipline areas! If possible another area where jobs related to these issues may be posted as project or job opportunities by potential employers.

If there is a way to create a feed from various job sites that already exist...like Nuvol...or http://www.verdantledgerhub.example/ that would be super great. Again...sort of a portal connection to bridge the gap ....instead of candidates having to search all the time, we are hoping they can advertise their talent and employers may search here for these well presented portfolios!

Target Market(s)

Educators, Students, Career Transitioners, Employers, Professional Associations, Talent Recruiters with focus on Sustainability related Talent to Task matching!

Industry/Entity Type

Sustainability

Number of Pages Required

4 page

Font styles to use
Sans Serif

Colors
3176b5
32b8a4
add136

Requirements
Must have
• Not sure about the coded/ uncoded option here....
• Must have - grid style area where Sustainability Professionals with varied focus areas can exhibit their talent portfolios
• appear as a Talent Gallery that starts with photos & obvious organization...other tabs to be in a menu.
• ability to search both talent and task opportunity areas to help coaches or community members make matches....some topic focused category or tag words to help make them searchable...???
• consistent professional styling to existing website and new pixelmarket postcard shared in brief/ images area
• Interactive blog space where articles, issues may be posted, discussed
• Bulletin board or feed for project opportunities to be posted where candidates may locate them and/or employers may express specific "call" for talent..These may be Short term Internships, Projects, Consulting Team Opportunity, or Jobs/ part time to full time....
Nice to have
• A calendar area where we can post networking opportunities, issues presentations where potential partners can meet the next generation leaders, attend a forum or webinar presentation.
Should not have
• Too much text on front page...Should be clean design,

```html
<!DOCTYPE html>
<html lang="en">
<head>
<meta charset="utf-8">
<title>VocaTerrania</title>
<link href="https://fonts.googleapis.com/css2?family=Open+Sans:wght@400;600;700&family=Raleway:wght@300;400;600&display=swap" rel="stylesheet">
<style>
:root{
  --blue:#3176b5;
  --blue-bright:#1a8fd8;
  --teal:#32b8a4;
  --lime:#add136;
  --ink:#333a40;
  --muted:#8a9299;
  --line:#e3e6e9;
  --soft:#f3f4f6;
  --white:#ffffff;
}
*{box-sizing:border-box;margin:0;padding:0}
html,body{width:1200px;height:2272px;overflow:hidden;background:var(--white);font-family:"Open Sans",Arial,sans-serif;color:var(--ink)}
.page{position:relative;width:1200px;height:2272px}
.topbar{height:32px;background:var(--blue-bright);color:var(--white);font-size:11px;display:flex;align-items:center;justify-content:space-between;padding:0 60px}
.topbar .contact{display:flex;gap:22px}
.topbar .social{display:flex;gap:8px}
.topbar .social span{width:12px;height:12px;border-radius:50%;background:rgba(255,255,255,.75)}
.navbar{height:48px;display:flex;align-items:center;justify-content:space-between;padding:0 60px;border-bottom:1px solid var(--line)}
.brand{display:flex;align-items:center;gap:8px;font-size:16px;font-weight:600;color:var(--blue)}
.brand .dot{width:18px;height:18px;border-radius:50%;background:var(--teal)}
.menu{display:flex;gap:20px;font-size:11px;font-weight:600;color:var(--ink)}
.menu .active{color:var(--blue-bright)}
.hero{position:relative;height:512px;overflow:hidden}
.hero .photo{position:absolute;inset:0;background:linear-gradient(135deg,#6d5a46 0%,#9c8670 40%,#d7d4cd 70%,#eceae5 100%)}
.hero svg{position:absolute;inset:0}
.hero .copy{position:absolute;left:60px;top:180px;color:var(--white);width:440px}
.hero h1{font-family:"Raleway",sans-serif;font-weight:600;font-size:40px;letter-spacing:1px}
.hero p{font-size:12px;line-height:1.6;margin-top:12px;opacity:.9}
.btn{display:inline-block;background:var(--blue-bright);color:var(--white);font-size:12px;font-weight:600;padding:9px 22px;border-radius:3px;border:1px solid rgba(255,255,255,.5)}
.hero .btn{margin-top:26px}
.hero .arrow{position:absolute;top:240px;width:26px;height:26px;color:var(--white);font-size:22px;opacity:.8}
.about{height:388px;display:flex;align-items:center;gap:40px;padding:0 60px}
.about .text{width:560px}
.section-title{font-family:"Raleway",sans-serif;font-weight:400;font-size:32px;color:var(--ink)}
.about .text p{font-size:12px;line-height:1.7;color:var(--muted);margin:18px 0 26px}
.ph{display:block}
.about .resume{width:220px;height:240px;background:linear-gradient(160deg,#c9ccd0,#7c7f84)}
.about .team{width:220px;height:240px;background:linear-gradient(160deg,#7fa35c,#3f6f3a)}
.portfolio{background:var(--soft);height:340px;padding:26px 60px 0}
.tabs{display:flex;gap:18px;margin:14px 0 16px;font-size:10px;font-weight:600;color:var(--muted)}
.tabs span{padding:4px 10px}
.tabs .on{background:var(--lime);color:var(--white);border-radius:2px}
.grid{display:grid;grid-template-columns:repeat(4,1fr);gap:0;height:210px}
.grid .g1{background:linear-gradient(135deg,#4d6e9a,#b7c4d6)}
.grid .g3{background:linear-gradient(135deg,#d3a4a8,#e8e2dd 60%,#7a8a9b)}
.grid .g4{background:linear-gradient(135deg,#f1f2f4,#9aa2ab)}
.feature{background:var(--blue-bright);color:var(--white);display:flex;flex-direction:column;align-items:center;justify-content:center;text-align:center;padding:0 30px}
.feature h3{font-size:14px;font-weight:700;letter-spacing:1px}
.feature p{font-size:10px;line-height:1.6;margin:8px 0;opacity:.9}
.feature .more{font-size:11px;font-weight:600}
.blog{height:500px;padding-top:34px;text-align:center}
.cards{display:flex;justify-content:center;gap:20px;margin-top:24px;text-align:left}
.card{width:420px}
.card .ph{height:252px}
.card.c1 .ph{background:linear-gradient(135deg,#c8d6e4,#6f8aa8)}
.card.c2 .ph{background:linear-gradient(135deg,#e7e9ec,#8b959f)}
.card .body{display:flex;gap:14px;margin-top:18px}
.date{width:48px;text-align:center;color:var(--blue-bright);font-weight:700;font-size:22px;line-height:1}
.date small{display:block;font-size:10px;font-weight:600;color:var(--muted);margin-top:4px}
.card h4{font-size:14px;color:var(--blue-bright);font-weight:700}
.card .meta{font-size:9px;color:var(--muted);margin:4px 0 10px}
.card p{font-size:11px;line-height:1.7;color:var(--muted)}
.partners{height:180px;border-top:1px solid var(--line);display:flex;justify-content:center;align-items:center;gap:22px}
.partner{width:168px;height:72px;border:1px solid var(--line);display:flex;align-items:center;justify-content:center;gap:8px}
.partner i{width:20px;height:20px;border-radius:50%;background:#c9ced3}
.partner b{width:54px;height:8px;background:#d7dbdf}
.partner.hi i{background:var(--teal)}
.partner.hi b{background:var(--blue)}
.footer{height:240px;background:var(--soft);display:grid;grid-template-columns:300px 220px 260px 240px;gap:0 20px;padding:40px 60px 0}
.footer h5{font-size:12px;font-weight:700;margin-bottom:12px;letter-spacing:.5px}
.footer p,.footer li{font-size:10px;line-height:1.7;color:var(--muted);list-style:none}
.footer .brand{margin-bottom:10px}
.input{display:flex;margin:10px 0}
.input span{flex:1;height:28px;background:var(--white);border:1px solid var(--line);font-size:10px;color:var(--muted);padding:6px 8px}
.input b{width:34px;height:28px;background:var(--blue-bright)}
.pager{display:flex;gap:6px}
.pager span{width:18px;height:18px;border-radius:50%;border:1px solid var(--line);font-size:9px;text-align:center;line-height:16px;color:var(--muted)}
.pager .on{background:var(--lime);border-color:var(--lime);color:var(--white)}
.ci{display:flex;gap:8px;align-items:center;margin-bottom:6px;font-size:10px;color:var(--muted)}
.ci svg{flex:none}
.bottom{height:32px;background:var(--blue-bright);color:var(--white);font-size:10px;display:flex;align-items:center;justify-content:center}
</style>
</head>
<body>
<div class="page">
  <div class="topbar">
    <div class="contact"><span>✆ +1 555 0142 000</span><span>✉ hello@vocaterrania.example</span></div>
    <div class="social"><span></span><span></span><span></span><span></span></div>
  </div>
  <header class="navbar">
    <div class="brand"><span class="dot"></span>VocaTerrania</div>
    <nav class="menu"><span class="active">HOME</span><span>ABOUT</span><span>PORTFOLIO</span><span>BLOG</span><span>CONTACT</span></nav>
  </header>

  <section class="hero">
    <div class="photo ph" role="img" aria-label="Team of professionals working over documents and laptops at a desk"></div>
    <svg width="1200" height="512" viewBox="0 0 1200 512" aria-hidden="true">
      <defs><linearGradient id="hb" x1="0" y1="0" x2="1" y2="1"><stop offset="0" stop-color="#2a8fd6"/><stop offset="1" stop-color="#1572c2"/></linearGradient></defs>
      <polygon points="0,0 560,0 720,512 0,512" fill="url(#hb)" opacity=".95"/>
      <polygon points="0,410 1200,300 1200,512 0,512" fill="#3aa3e6" opacity=".55"/>
      <polygon points="0,455 1200,395 1200,512 0,512" fill="#1a8fd8" opacity=".9"/>
    </svg>
    <span class="arrow" style="left:14px">‹</span>
    <span class="arrow" style="right:6px">›</span>
    <div class="copy">
      <h1>VOCATERRANIA</h1>
      <p>A shared space where sustainability talent meets real projects, partners and coaching across every focus area.</p>
      <span class="btn">Read More</span>
    </div>
  </section>

  <section class="about">
    <div class="text">
      <h2 class="section-title">About Us</h2>
      <p>VocaTerrania brings together educators, students, career changers and employers around sustainability work. Candidates build clear portfolios with resumes, biographies and case studies, then link them to focus areas such as energy, water, public health and sustainable cities. Coaches and community members can search talent and open tasks side by side, while employers post internships, projects and roles. Our aim is simple: fewer hours spent searching, more time spent matching the right people with the right work.</p>
      <span class="btn">Read More</span>
    </div>
    <div class="resume ph" role="img" aria-label="Hands holding a printed resume"></div>
    <div class="team ph" role="img" aria-label="Group of young professionals gathered outdoors"></div>
  </section>

  <section class="portfolio">
    <h2 class="section-title">Portfolio</h2>
    <div class="tabs"><span class="on">ALL</span><span>PUBLIC HEALTH</span><span>TECHNOLOGY</span><span>INFRASTRUCTURE</span><span>EDUCATION</span><span>POLICY</span><span>ENERGY</span></div>
    <div class="grid">
      <div class="g1 ph" role="img" aria-label="Open book lying on a table"></div>
      <div class="feature">
        <h3>TRAINING COURSES</h3>
        <p>Short guided courses that help you shape a strong sustainability portfolio.</p>
        <span class="more">Read More →</span>
      </div>
      <div class="g3 ph" role="img" aria-label="Tablet and colour swatches on a desk"></div>
      <div class="g4 ph" role="img" aria-label="Computer monitor on a clean white workspace"></div>
    </div>
  </section>

  <section class="blog">
    <h2 class="section-title">Walking the Ridge</h2>
    <div class="cards">
      <article class="card c1">
        <div class="ph" role="img" aria-label="Business team celebrating in an office"></div>
        <div class="body">
          <div class="date">14<small>JUL</small></div>
          <div>
            <h4>Contrary to popular belief.</h4>
            <div class="meta">By admin | In Sustainability | 3 Comments</div>
            <p>Cross-discipline partners often solve what single fields cannot. Here we look at energy and water teams sharing one brief.</p>
          </div>
        </div>
      </article>
      <article class="card c2">
        <div class="ph" role="img" aria-label="Colleagues reviewing charts at a meeting table"></div>
        <div class="body">
          <div class="date">14<small>JUL</small></div>
          <div>
            <h4>Contrary to popular belief.</h4>
            <div class="meta">By admin | In Careers | 5 Comments</div>
            <p>Employers now look for clear case studies. A short guide on presenting project results inside your talent portfolio.</p>
          </div>
        </div>
      </article>
    </div>
  </section>

  <section class="partners">
    <div class="partner"><i></i><b></b></div>
    <div class="partner"><i></i><b></b></div>
    <div class="partner hi"><i></i><b></b></div>
    <div class="partner"><i></i><b></b></div>
    <div class="partner"><i></i><b></b></div>
  </section>

  <footer class="footer">
    <div>
      <div class="brand"><span class="dot"></span>VocaTerrania</div>
      <p>A community portal linking sustainability talent with projects, partners and mentors. Share your work, find open calls and grow your network in one place.</p>
    </div>
    <div>
      <h5>COURSES LINKS</h5>
      <ul><li>Water Systems</li><li>Urban Design</li><li>Public Health</li><li>Green Policy</li><li>Ecosystems</li><li>Energy Design</li></ul>
    </div>
    <div>
      <h5>NEWSLETTER</h5>
      <p>Subscribe to our newsletter to get latest updates and news.</p>
      <div class="input"><span>Enter email</span><b></b></div>
      <div class="pager"><span class="on">1</span><span>2</span><span>3</span></div>
    </div>
    <div>
      <h5>CONTACT</h5>
      <div class="ci"><svg width="10" height="12" viewBox="0 0 10 12"><path d="M5 0a4 4 0 0 1 4 4c0 3-4 8-4 8S1 7 1 4a4 4 0 0 1 4-4z" fill="#8a9299"/></svg>48 Fernvale Row, Suite 12, Brookmere</div>
      <div class="ci"><svg width="10" height="10" viewBox="0 0 10 10"><path d="M2 0l2 2-1 2 3 3 2-1 2 2-2 2C4 10 0 6 0 2z" fill="#8a9299"/></svg>+1 555 0142 000</div>
      <div class="ci"><svg width="12" height="9" viewBox="0 0 12 9"><rect x=".5" y=".5" width="11" height="8" fill="none" stroke="#8a9299"/><path d="M.5.5 6 5l5.5-4.5" fill="none" stroke="#8a9299"/></svg>hello@vocaterrania.example</div>
    </div>
  </footer>
  <div class="bottom">Copyright 2016. All Right Reserved</div>
</div>
</body>
</html>
```